Web Design for High End Baby Products Gear

We have some work from a designer that just didn't meet standards despite weeks of back and forth. We need someone who can come up with creative colors/fonts/etc. to make the site "pop" and give a clean, inviting feel.

We need three pages designed:

1. Home
2. Category Landing Page
3. Product Detail Page

The current site is www.PramTrailWorks.com

Please DO NOT use current site for inspiration.

The layout should follow pretty close to what we have attached.

We were not even pleased with the logo so for now we are just concentrating on the colors and aesthetic feel of the site. You can use a nice typography type logo. We will probably have the logo done at a later time. Or if you have any ideas please feel free to submit as it may increase chances of winning design. The layout is pretty much done with the product page layout approved by our paid search people.

This is isn't where you need to spend a lot of time with general layout as it is already pretty much complete but you are free to deviate or make suggestions if you think it will help.

Reason: I haven't been able to provide adequate feedback and want to spend appropriate amount of time doing so.

I posted the set of PSD files that the previous designer completed.  We were not happy with the outcome of this.

I said in my brief "Here are a few like companies:

www.wheelnestshop.com
www.cradlelane.com
www.tumbleferntots.com
www.qorvix.com
www.dapplemoss.com
www.ovarenti.com"

What I meant was that these were similar companies to our company with respect to product/customer demographic/etc.

Reason: We have found a few that we really like and are working to determine which designs to continue with.

Thank you for your patience.

Reason: Waiting on feedback from a couple of designers so extending deadline

Thank you all.  We received several designs we really liked.  A couple stood out more than others as they seemed to hit the target on the first go around based on our brief and sample sites submitted.

There are several designers we would like to work with in the future as well as we have about 40 domains we will be developing.

Thank you.

Target Market(s)

Target Market: Female, typically 25-40 yrs old, probably married, probably career minded OR middle to upper middle income (some of our strollers are $500-$1,200), expecting mom or mom, some might have two stroller aged (double strollers). Some of our products are QUALITY (KIV for jogging or running) or QUALITY with STYLE (Fennamor), but the truth is that this is a WANT not a need. Sure people need A stroller but not a $900 Tamsel Stroller. So they have a combination of want and need coupled with ability to pay.

Brand Personality:
Definitely clean, crisp and modern. We want it to “POP” but in color and style. But I guess more directly is we want to be seen as THE or ONE of THE authorities on upper end strollers. Where you can get individual assistance, stroller consultations (yes people call in with their needs and ask advice) and personalized service as opposed to a “big box” type place that tries to be everything to everyone and when you call them you get some guy in a cubicle answering the phone that held his baby niece once. So when someone hits our site or walks into our showroom, they need to know they are in the right place.

Industry/Entity Type

Baby

Requirements
Must have
• Must a clean crisp color scheme, easy to ready, focused on products. Must instill authority, credibility, usability and be simple and uncluttered. Fonts and colors must complement each other to achieve the above.

We need three main images as well for the home page as they will be sliding/rotating images.

Backend is built in Corvane so design must conform to that platform.

We retain exlusive rights to the design and all files
Nice to have
• Please see attached word file for more info.

Here are some sites we like:

www.tinyharbor.com
http://www.cubgrove.com/
http://www.fernlark.com/
http://www.quendatots.com/index.php
http://www.pavrel.com/
http://www.vend-arle.com/
http://www.gorbly.com/
http://www.partycardworkshop.com/

Keep in mind that I may just like only something about the above sites and not everything. It may be color, it may be layout , font color, use of text on home page, but something about them stands out.

Here are a few like companies:

www.wheelnestshop.com
www.cradlelane.com
www.tumbleferntots.com
www.qorvix.com
www.dapplemoss.com
www.ovarenti.com
Should not have
• old dated styles, nothing "frilly"

```html
<!DOCTYPE html>
<html lang="en">
<head>
<meta charset="utf-8">
<title>PramTrail Works – Product Detail</title>
<link rel="stylesheet" href="https://fonts.googleapis.com/css2?family=Arimo:wght@400;700&family=Noto+Sans:wght@400;700&display=swap">
<style>
:root{
  --green:#8cc400;
  --green-dark:#76a800;
  --orange:#f7941d;
  --grey-text:#555;
  --muted:#8a8a8a;
  --line:#d6d6d6;
  --footer:#303030;
  --footer-text:#e6e6e6;
  --page:#ffffff;
}
*{box-sizing:border-box;margin:0;padding:0}
html,body{width:1200px;height:933px;overflow:hidden;background:var(--page)}
body{position:relative;font-family:"Noto Sans",Verdana,sans-serif;color:var(--grey-text);font-size:12.5px;
  background:linear-gradient(#fff 0,#f4f4f4 260px,#fff 560px)}
.abs{position:absolute}
.top-rule{left:0;top:0;width:1200px;height:3px;background:var(--green)}
.logo{left:38px;top:22px;font-family:Arimo,Arial,sans-serif;font-weight:700;font-size:41px;line-height:48px;color:var(--green)}
.perks{left:500px;top:29px;width:200px;height:87px;border:1px solid #ccc;border-radius:4px;background:#fff;padding:9px 0 0 13px;list-style:none;font-size:13px;line-height:17px;color:#555}
.perks li{display:flex;align-items:center;gap:6px}
.search{left:878px;top:24px;width:284px;height:28px;border:1px solid var(--green);border-radius:4px;background:#fff;display:flex;align-items:center;justify-content:space-between;padding:0 6px 0 8px;font-size:12.5px;color:#444}
.phone{left:880px;top:60px;width:282px;text-align:center;font-family:Arimo,Arial,sans-serif;font-weight:700;font-size:31px;color:var(--orange)}
.phone-alt{left:880px;top:96px;width:282px;text-align:center;font-family:Arimo,Arial,sans-serif;font-weight:700;font-size:24px;color:#888}
.nav{left:38px;top:142px;width:1124px;height:40px;background:var(--green);border-radius:9px;display:flex;align-items:center;padding:0 10px 0 22px}
.nav a{color:#fff;text-decoration:none;font-size:13.5px}
.nav .sep{color:#fff;margin:0 6px;font-size:13px}
.nav .tools{margin-left:auto;display:flex;align-items:center;gap:6px}
.social-chip{font-size:10px;color:#fff;display:flex;align-items:center;gap:3px}
.social-chip i{display:block;width:14px;height:14px;background:#fff;opacity:.85}
.view-cart{width:80px;height:20px;border-radius:4px;background:#fff;color:#444;font-size:12.5px;text-align:center;line-height:20px;margin-left:8px}
.newsletter{left:38px;top:193px;width:194px;height:103px;border:1px solid #ccc;border-radius:3px;background:linear-gradient(#fff,#eee);text-align:center;padding-top:9px}
.newsletter p{color:#29a8e0;font-weight:700;font-size:15.5px;line-height:19px}
.newsletter strong{display:block;color:var(--orange);font-family:Arimo,Arial,sans-serif;font-size:43px;line-height:48px}
.side-heading{font-size:20.5px;color:var(--green)}
.select{width:144px;height:18px;border:1px solid #999;background:#fff;font-size:12px;color:#333;display:flex;justify-content:space-between;align-items:center;padding-left:3px}
.select b{width:17px;height:16px;background:#ddd;border-left:1px solid #999;display:flex;align-items:center;justify-content:center}
.cat-list{left:55px;top:407px;list-style:none;font-size:12.5px;color:#555}
.cat-list li{height:21px;display:flex;align-items:center;gap:9px}
.product-title{left:241px;top:186px;font-size:27px;color:var(--green)}
.product-photo{left:336px;top:258px;width:262px;height:344px;background:radial-gradient(ellipse at 50% 45%,#e14640 0,#c9302a 30%,#6a6a6a 55%,#f3f3f3 80%)}
.buy-panel{left:686px;top:193px;width:476px;height:410px;border:1px solid var(--line);background:#fff}
.price-row{position:absolute;left:10px;top:17px;font-size:16px;color:#555}
.price-old{position:absolute;left:67px;top:16px;font-size:19px;color:#666;text-decoration:line-through}
.price-new{position:absolute;left:67px;top:41px;font-size:19px;color:var(--orange)}
.save{position:absolute;left:150px;top:41px;font-size:19px;color:#555}
.specs{position:absolute;left:10px;top:81px;font-size:12.5px;line-height:17px;color:#555}
.specs div{display:flex}
.specs span:first-child{width:100px;text-align:right;margin-right:6px}
.divider{position:absolute;left:0;width:100%;height:1px;background:var(--line)}
.opt-label{position:absolute;font-size:13px;color:#555}
.color-select{position:absolute;left:70px;top:165px;width:144px;height:18px}
.qty{position:absolute;left:70px;top:190px;width:45px;height:18px;border:1px solid #7aa3c8;font-size:12px;padding-left:12px;line-height:16px}
.add-cart{position:absolute;left:226px;top:165px;width:106px;height:26px;background:var(--green);color:#fff;font-size:12.5px;text-align:center;line-height:26px;text-decoration:underline}
.registry{position:absolute;left:344px;top:165px;font-size:12.5px;color:#333;text-decoration:underline;display:flex;gap:6px;align-items:center}
.review{position:absolute;left:12px;top:232px;display:flex;align-items:center;gap:8px;font-size:13px;color:#1b4f9c}
.share-grid{position:absolute;left:12px;top:272px;width:456px;display:grid;grid-template-columns:176px 138px 140px;row-gap:11px;font-size:13px;color:#1b4f9c}
.share-grid span{display:flex;align-items:center;gap:7px;height:21px}
.share-grid i{display:block;width:15px;height:15px;border-radius:2px}
.util-row{position:absolute;left:16px;top:377px;display:flex;gap:26px;font-size:13px;color:#1b4f9c}
.util-row span{display:flex;align-items:center;gap:7px}
.tabs{left:244px;top:626px;width:918px;height:132px;border:1px solid var(--line);background:#fff}
.tab-row{display:flex;height:29px}
.tab{padding:0 6px;line-height:29px;font-size:12.5px;color:#444;background:#e1e1e1;border-right:1px solid #fff}
.tab.active{background:#f4f4f4;border:1px solid var(--line);border-top:none;border-left:none}
.tab-body{padding:6px 11px;font-size:12.5px;line-height:17px;color:#555;border-top:1px solid var(--line)}
.footer{left:0;top:781px;width:1200px;height:152px;background:var(--footer);color:var(--footer-text)}
.foot-col{position:absolute;top:20px;font-size:13px;line-height:17px}
.foot-col h4{font-size:13px;font-weight:700;margin-bottom:17px;color:#fff}
.cards{position:absolute;left:890px;top:23px;display:flex;gap:10px}
.card{width:61px;height:37px;border-radius:3px;background:#f0f0f0;color:#333;font-size:11px;display:flex;align-items:center;justify-content:center}
.legal{position:absolute;right:38px;top:112px;font-size:12.5px;color:#ccc}
</style>
</head>
<body>
<div class="abs top-rule"></div>

<header>
  <div class="abs logo">PramTrail<br>Works</div>
  <ul class="abs perks">
    <li><svg width="14" height="12"><path d="M1 6l4 4 8-9" stroke="#8cc400" stroke-width="3" fill="none"/></svg>365 Day Returns</li>
    <li><svg width="14" height="12"><path d="M1 6l4 4 8-9" stroke="#8cc400" stroke-width="3" fill="none"/></svg>Free Shipping</li>
    <li><svg width="14" height="12"><path d="M1 6l4 4 8-9" stroke="#8cc400" stroke-width="3" fill="none"/></svg>No Sales Tax</li>
    <li><svg width="14" height="12"><path d="M1 6l4 4 8-9" stroke="#8cc400" stroke-width="3" fill="none"/></svg>Parice Match Guarantee</li>
  </ul>
  <div class="abs search">search keyword here...
    <svg width="20" height="20"><circle cx="8" cy="8" r="6" stroke="#8cc400" stroke-width="3" fill="none"/><path d="M12 12l6 6" stroke="#8cc400" stroke-width="3"/></svg>
  </div>
  <div class="abs phone">1-800-PRAMS-00</div>
  <div class="abs phone-alt">(800-555-0199)</div>
  <nav class="abs nav">
    <a>Home</a><span class="sep">|</span><a>Gift Registry</a><span class="sep">|</span><a>Gift Cards</a><span class="sep">|</span><a>Contact Us</a><span class="sep">|</span><a>Store Location</a><span class="sep">|</span><a>Blog</a><span class="sep">|</span><a>Registry</a><span class="sep">|</span><a>Check Out</a><span class="sep">|</span><a>My Account</a>
    <div class="tools">
      <span class="social-chip"><i></i>Pally</span>
      <span class="social-chip"><i></i>Chirpo</span>
      <svg width="26" height="22"><path d="M3 8h20l-2 12H5z" fill="#f2c04a"/><path d="M3 8l5-5h10l5 5" fill="#e0a530"/></svg>
      <span class="view-cart">view cart</span>
    </div>
  </nav>
</header>

<aside>
  <div class="abs newsletter"><p>Sign Up for our<br>Newsletter &amp; SAVE</p><strong>5% Off</strong></div>
  <h3 class="abs side-heading" style="left:37px;top:303px">Shop by Brands</h3>
  <div class="abs select" style="left:38px;top:335px">Select a Brand:<b><svg width="9" height="6"><path d="M0 0h9L4.5 6z" fill="#333"/></svg></b></div>
  <h3 class="abs side-heading" style="left:37px;top:372px">Shop by Catergories</h3>
  <ul class="abs cat-list">
    <li><svg width="7" height="8"><path d="M0 0l7 4-7 4" fill="none" stroke="#8cc400" stroke-width="1.5"/></svg>Tot Trotter</li>
    <li><svg width="7" height="8"><path d="M0 0l7 4-7 4" fill="none" stroke="#8cc400" stroke-width="1.5"/></svg>KIV Stroller</li>
    <li><svg width="7" height="8"><path d="M0 0l7 4-7 4" fill="none" stroke="#8cc400" stroke-width="1.5"/></svg>Fennamor Stroller</li>
    <li><svg width="7" height="8"><path d="M0 0l7 4-7 4" fill="none" stroke="#8cc400" stroke-width="1.5"/></svg>Wispride Stroller</li>
    <li><svg width="7" height="8"><path d="M0 0l7 4-7 4" fill="none" stroke="#8cc400" stroke-width="1.5"/></svg>Halvic Stroller</li>
    <li><svg width="7" height="8"><path d="M0 0l7 4-7 4" fill="none" stroke="#8cc400" stroke-width="1.5"/></svg>Ivlo Stroller</li>
    <li><svg width="7" height="8"><path d="M0 0l7 4-7 4" fill="none" stroke="#8cc400" stroke-width="1.5"/></svg>Mom or Mom</li>
    <li><svg width="7" height="8"><path d="M0 0l7 4-7 4" fill="none" stroke="#8cc400" stroke-width="1.5"/></svg>Ridgeway Buggy</li>
    <li><svg width="7" height="8"><path d="M0 0l7 4-7 4" fill="none" stroke="#8cc400" stroke-width="1.5"/></svg>Tamsel Baby Stroller</li>
    <li><svg width="7" height="8"><path d="M0 0l7 4-7 4" fill="none" stroke="#8cc400" stroke-width="1.5"/></svg>Bright Star Stroller</li>
    <li><svg width="7" height="8"><path d="M0 0l7 4-7 4" fill="none" stroke="#8cc400" stroke-width="1.5"/></svg>Tot Trotter</li>
    <li><svg width="7" height="8"><path d="M0 0l7 4-7 4" fill="none" stroke="#8cc400" stroke-width="1.5"/></svg>KIV Stroller</li>
  </ul>
</aside>

<main>
  <h1 class="abs product-title" style="font-weight:400">Product Title goes here</h1>
  <div class="abs product-photo" role="img" aria-label="Product photo: red three-wheel jogging stroller"></div>

  <section class="abs buy-panel">
    <span class="price-row">Price :</span>
    <span class="price-old">$699.00</span>
    <span class="price-new">$600.00</span>
    <span class="save">You Save 16%</span>
    <div class="specs">
      <div><span>SKU :</span><span>BG031</span></div>
      <div><span>Item Number :</span><span>BG123456</span></div>
      <div><span>UPC :</span><span>1234567898123</span></div>
    </div>
    <div class="divider" style="top:152px"></div>
    <span class="opt-label" style="left:18px;top:166px">Color :</span>
    <div class="select color-select">Select a Color<b><svg width="9" height="6"><path d="M0 0h9L4.5 6z" fill="#333"/></svg></b></div>
    <span class="opt-label" style="left:29px;top:192px">Qty :</span>
    <div class="qty">1</div>
    <div class="add-cart">add to cart</div>
    <div class="registry"><svg width="16" height="16"><path d="M8 1v14M1 8h14" stroke="#8cc400" stroke-width="4"/></svg>Add to Registry</div>
    <div class="divider" style="top:220px"></div>
    <div class="review"><svg width="18" height="18"><rect x="1" y="1" width="12" height="15" fill="#fff" stroke="#999"/><circle cx="10" cy="10" r="4" fill="none" stroke="#4a7cc0" stroke-width="1.5"/><path d="M13 13l4 4" stroke="#4a7cc0" stroke-width="2"/></svg>Review this Product</div>
    <div class="divider" style="top:260px;left:12px;width:452px;background:none;border-top:1px dotted #bbb"></div>
    <div class="share-grid">
      <span><i style="background:#3a6fd0"></i>Savorly</span>
      <span><i style="background:#777"></i>Quorra</span>
      <span><i style="background:#f2c300"></i>Bookmark</span>
      <span><i style="background:#5b9a3a"></i>Tripalong</span>
      <span><i style="background:#7b2b9a"></i>Hollerly</span>
      <span><i style="background:#35a4dd"></i>Chirpo</span>
      <span><i style="background:#555"></i>Threadle</span>
      <span><i style="background:#999"></i>Delvo</span>
      <span><i style="background:#f06a1d"></i>Postnook</span>
    </div>
    <div class="divider" style="top:367px;left:12px;width:452px;background:none;border-top:1px dotted #bbb"></div>
    <div class="util-row">
      <span><svg width="20" height="16"><circle cx="10" cy="6" r="5" fill="#f5a623"/><rect x="3" y="10" width="14" height="5" fill="#d0392b"/></svg>Guaranteed</span>
      <span style="margin-left:2px"><svg width="18" height="14"><rect x="1" y="2" width="16" height="11" fill="#f6d58a" stroke="#c9a24a"/><path d="M1 2l8 6 8-6" fill="none" stroke="#c9a24a"/></svg>Email</span>
      <span style="margin-left:18px"><svg width="18" height="16"><rect x="4" y="1" width="10" height="5" fill="#fff" stroke="#777"/><rect x="1" y="6" width="16" height="7" fill="#9aa6b4"/><rect x="4" y="11" width="10" height="4" fill="#fff" stroke="#777"/></svg>Print</span>
    </div>
  </section>

  <section class="abs tabs">
    <div class="tab-row">
      <span class="tab active">Product Description</span>
      <span class="tab">Technical Specs</span>
      <span class="tab">Customer Reviews</span>
    </div>
    <p class="tab-body">Lorem Ipsum has been the industry's standard dummy text ever since the 1500s, when an unknown printer took a galley of type and scrambled it to make a type specimen book. It has survived not only five centuries, but also the leap into electronic typesetting, remaining essentially unchanged. It was popularised in the 1960s with the release of Varnoset sheets containing Lorem Ipsum passages, and more recently with desktop publishing software like Orrin PageSetter including versions of Lorem Ipsum.</p>
  </section>
</main>

<footer class="abs footer">
  <div class="foot-col" style="left:37px"><h4>Company Info</h4>About Us<br>Contact Us<br>Sitemap</div>
  <div class="foot-col" style="left:197px"><h4>Customer Care</h4>Contact Us<br>Price matching<br>Testimonials</div>
  <div class="foot-col" style="left:365px"><h4>Export Outdoor Advice</h4>Expert Advice Articles<br>Out Door Videos<br>Store Events</div>
  <div class="foot-col" style="left:588px"><h4>Help</h4>Live Help<br>Order Status<br>Return and Exchange</div>
  <div class="cards">
    <span class="card">Meridan</span><span class="card">Vantra</span><span class="card">Amerion</span><span class="card">Dovecard</span>
  </div>
  <div class="legal">© 2011 Baby Products &nbsp;&nbsp; | &nbsp;&nbsp; Terms and Conditions</div>
</footer>
</body>
</html>
```